Business card for a new cabinet shop company named Marlowe Cabinets for high end cabinets

Design a business card, thinking dark rich green with colours to speak of high end luxury ie; cream, gold, black possibly

Peter Lindqvar
Director Craftsman
Email: info@marlowecabinets.com.au
Instagram : @marlowe.cabinets

```html
<!DOCTYPE html>
<html lang="en">
<head>
<meta charset="utf-8">
<title>Marlowe Cabinets — Business Card</title>
<link href="https://fonts.googleapis.com/css2?family=Poppins:wght@400;500;600&display=swap" rel="stylesheet">
<style>
  :root {
    --backdrop: #c8a964;
    --card-green: #08402c;
    --gold: #c9a45c;
    --cream: #e6e2d6;
    --faint-mark: #3e5a33;
  }
  * { box-sizing: border-box; margin: 0; padding: 0; }
  html, body {
    width: 1200px; height: 900px; overflow: hidden;
    background: var(--backdrop);
    font-family: "Poppins", sans-serif;
  }
  .canvas { position: relative; width: 1200px; height: 900px; }
  .card {
    position: absolute;
    width: 580px; height: 331px;
    background: var(--card-green);
    box-shadow: 0 6px 18px rgba(60, 40, 10, 0.28);
    overflow: hidden;
  }
  .card--front { left: 110px; top: 120px; }
  .card--back { left: 510px; top: 450px; }

  .brand {
    position: absolute; left: 50%; top: 50%;
    transform: translate(-50%, -50%);
    display: flex; align-items: center; gap: 18px;
    white-space: nowrap;
  }
  .brand__square {
    width: 40px; height: 40px;
    border: 3px solid var(--gold);
  }
  .brand__name {
    color: var(--gold);
    font-weight: 500; font-size: 38px; letter-spacing: 1px;
  }

  .holder {
    position: absolute; right: 44px; top: 52px;
    text-align: right;
  }
  .holder__name {
    color: var(--gold);
    font-weight: 600; font-size: 22px; letter-spacing: 0.5px;
    text-transform: uppercase; line-height: 1.15;
  }
  .holder__title {
    color: var(--cream);
    font-weight: 400; font-size: 15px;
    padding-bottom: 6px;
    border-bottom: 1.5px solid var(--gold);
  }

  .contact {
    position: absolute; right: 44px; top: 148px;
    list-style: none;
    color: var(--cream); font-size: 12.5px; line-height: 1.3;
  }
  .contact__item {
    display: flex; justify-content: flex-end; align-items: center;
    gap: 10px; margin-bottom: 6px;
  }
  .contact__icon { width: 16px; height: 16px; flex: none; }
  .contact__square { width: 14px; height: 14px; background: var(--gold); border-radius: 3px; flex: none; margin: 0 1px; }

  .faint-mark {
    position: absolute; left: 40px; bottom: 46px;
    display: flex; align-items: center; gap: 16px;
    color: var(--faint-mark);
    font-weight: 500; font-size: 34px; white-space: nowrap;
  }
  .faint-mark__square { width: 44px; height: 44px; border: 4px solid var(--faint-mark); }
</style>
</head>
<body>
<main class="canvas">
  <section class="card card--front" aria-label="Card front">
    <div class="brand">
      <span class="brand__square"></span>
      <span class="brand__name">Marlowe Cabinets</span>
    </div>
  </section>

  <section class="card card--back" aria-label="Card back">
    <div class="holder">
      <p class="holder__name">Peter Lindqvar</p>
      <p class="holder__title">Director Craftsman</p>
    </div>
    <ul class="contact">
      <li class="contact__item">
        <span>info@marlowecabinets.com.au</span>
        <svg class="contact__icon" viewBox="0 0 16 16" aria-hidden="true">
          <rect x="1" y="3" width="14" height="10" rx="1" fill="var(--gold)"/>
          <path d="M1.5 3.5 L8 9 L14.5 3.5" fill="none" stroke="var(--card-green)" stroke-width="1.3"/>
        </svg>
      </li>
      <li class="contact__item">
        <span>@marlowe.cabinets</span>
        <span class="contact__square"></span>
      </li>
    </ul>
    <div class="faint-mark" aria-hidden="true">
      <span class="faint-mark__square"></span>
      <span>Marlowe Cabinets</span>
    </div>
  </section>
</main>
</body>
</html>
```